PowerPoint Listing Presentation for Real Estate Agency

We need a PowerPoint presentation for a new real estate brokerage team.

[[[[[[submit 1-3 sample slides for review - i will provide feedback and you can make changes if you want to - we will not be deciding on a design prior to the deadline]]]]]

******ATTN: DESIGNERS, if your skills are webdesign then just look at this like a portable website or a brochure. it should be easy enough******

NOTE: we have all the data to put into the slides. You just need to come up with the design and layout. we have a sample design that we like and have provided.

This focus will be for the home listing side of the business (a presentation for home sellers to convince them to use our services). The data and slides will present our team and the benefits, in the best light, to use our services over that of other real estate agent applying for the job. This presentation will proved facts and benefits and describe our special and unique offerings that will show a home seller why we can sell their home for more money in less time and with the least amount of hassle. The main color scheme is Dark Blue and White (we want some additional colors included - based on your creativity. otherwise the presentation will too monotone). We would like to see the use of Statistical Graphs (3-D) - data provided. We have photos of our team and a new logo (the logo could have some minor adjustment to clean it up if necessary) - also uploaded. We have about 80-90% of the information that will be put into the slides and will need to work closely to get the design and data integrated into the presentation (should be easier then it sounds). We should be able to add slides and data 'at will' over time via our master slides built into the presentation. We have a pretty good sample presentation that we like and can be used as a guideline (this is from our affiliated business network and we have full rights to all the information), it is uploaded but doesn't contain all the slide because of size limitations.

NOTE: An additional buyers presentation will be needed after we get the sellers presentation completed, which means additional work.

This should be enough to get you started and we are available if you have any questions to help you with the project. there will be around 60-70 total slides. once concept is completed it will be easy to create the slides.

Target Market(s)

home sellers. people who are moving to a new and better home or relocation for job reasons. typically more established in life

Industry/Entity Type

Real Estate

Requirements
Must have
• all the slides must be congruent. in other words, the exact same layout feel should used across the board. we are working on building our trade dress/image. Also, it must have a soft and inviting overall feel, yet show strength of ability.
Nice to have
• nice to have use of real people images when necessary. 3D graphs would be nice. clean modern look and feel, yet sophisticated and professional.
Should not have
• should not have a lot of time consuming transitions. do not include 3D stick figures or distracting moving gifs

```html
<!DOCTYPE html>
<html lang="en">
<head>
<meta charset="utf-8">
<title>Our VIP Seller Benefits</title>
<link rel="stylesheet" href="https://fonts.googleapis.com/css2?family=Arvo:wght@700&family=Roboto:wght@700&display=swap">
<style>
  :root {
    --navy: #1b2035;
    --steel-light: #a9a9a9;
    --steel-mid: #8d8d8d;
    --steel-dark: #6e6e6e;
    --frame-line: #5a5a5a;
    --highlight: #ececec;
    --skin: #e8b89a;
    --roof: #5b4a44;
  }
  html, body {
    margin: 0;
    padding: 0;
    width: 1200px;
    height: 675px;
    overflow: hidden;
  }
  .slide {
    position: relative;
    width: 1200px;
    height: 675px;
    overflow: hidden;
    background: radial-gradient(ellipse at 55% 45%, var(--steel-light) 0%, var(--steel-mid) 60%, var(--steel-dark) 100%);
    font-family: "Arvo", Georgia, serif;
    color: var(--navy);
  }
  .slide-frame {
    position: absolute;
    inset: 12px;
    border: 2px solid var(--frame-line);
    pointer-events: none;
  }
  .title-band {
    position: absolute;
    left: 0;
    top: 0;
    width: 1200px;
    height: 92px;
    background: linear-gradient(180deg, #9b9b9b 0%, #7f7f7f 100%);
    border-bottom: 3px solid var(--frame-line);
    box-shadow: 0 3px 0 #b5b5b5;
  }
  .slide-title {
    position: absolute;
    left: 22px;
    top: 22px;
    margin: 0;
    font-size: 46px;
    line-height: 1;
    font-weight: 700;
    letter-spacing: 0.5px;
    color: var(--navy);
    text-shadow: 1px 1px 0 #c9c9c9;
  }
  .hero-photo {
    position: absolute;
    left: 0;
    top: 208px;
    width: 492px;
    height: 300px;
    background: linear-gradient(120deg, var(--skin) 0%, #d9a887 45%, #8a8580 70%, var(--roof) 100%);
    border-radius: 0 60px 60px 0;
    opacity: 0.9;
  }
  .benefit {
    position: absolute;
    left: 527px;
    display: flex;
    gap: 22px;
  }
  .benefit-marker {
    flex: none;
    width: 50px;
    height: 62px;
    background: var(--navy);
  }
  .benefit-text {
    margin: 0;
    font-size: 33px;
    line-height: 48px;
    font-weight: 700;
    text-shadow: 1px 1px 0 #b9b9b9;
  }
  .benefit--cash { top: 166px; }
  .benefit--buyback { top: 358px; }
  .indent { padding-left: 72px; }
  .accent { color: var(--highlight); text-shadow: none; }
  .accent-sans { font-family: "Roboto", Arial, sans-serif; }
  .brand-emblem {
    position: absolute;
    left: 982px;
    top: 390px;
    width: 200px;
    height: 260px;
  }
</style>
</head>
<body>
  <main class="slide">
    <header class="title-band">
      <h1 class="slide-title">Our VIP Seller Benefits</h1>
    </header>
    <div class="slide-frame"></div>

    <div class="hero-photo" role="img" aria-label="Photo of an open hand holding a small model house"></div>

    <section class="benefit benefit--cash">
      <span class="benefit-marker"></span>
      <p class="benefit-text">
        Your Home Sold at a Price<br>
        Acceptable to You <span class="accent">or</span><br>
        <span class="indent">We’ll Buy it for Cash!</span>
      </p>
    </section>

    <section class="benefit benefit--buyback">
      <span class="benefit-marker"></span>
      <p class="benefit-text">
        Buy Any One.<br>
        Not Satisfied?<br>
        <span class="accent-sans">WE’LL BUY IT BACK!</span><br>
        <span class="accent-sans">Till <span class="accent">24 Months</span></span>
      </p>
    </section>

    <svg class="brand-emblem" viewBox="0 0 200 260" aria-hidden="true">
      <rect x="10" y="20" width="180" height="230" fill="var(--navy)"/>
    </svg>
  </main>
</body>
</html>
```